professional business card

A Clean looking business card for a money transfer company. Our company is call Velorix= Transfer + Send = Transcend (next level)
to show professionalism as well as some effects to show digital tech.

1 side to have position, name and address
2 side to have company name and show that we provide money exchange and cross-border money transfer

Target Market(s)

Remittance companies and high net worth individuals

Industry/Entity Type

Finance

Contact Information for Business Card

Name, address, email, title, services- money exchange and cross-border remittance

Requirements
Nice to have
• Digital age feel

```html
<!DOCTYPE html>
<html lang="en">
<head>
<meta charset="utf-8">
<title>Velorix Business Card</title>
<link rel="stylesheet" href="https://fonts.googleapis.com/css2?family=Montserrat:wght@500;600;700&display=swap">
<style>
  :root {
    --page-bg: #d9dde0;
    --card-white: #ffffff;
    --ink-navy: #1f2d3d;
    --ink-muted: #5a6876;
    --accent-teal: #5bcbdc;
    --band-navy: #2a3a4a;
    --shadow: rgba(20, 30, 40, 0.22);
  }
  * { box-sizing: border-box; margin: 0; padding: 0; }
  html, body { width: 1200px; height: 750px; overflow: hidden; }
  body {
    background: var(--page-bg);
    font-family: "Montserrat", sans-serif;
    color: var(--ink-navy);
    display: flex;
    align-items: center;
    justify-content: center;
    gap: 60px;
  }
  .card {
    position: relative;
    width: 500px;
    height: 286px;
    background: var(--card-white);
    border-radius: 26px;
    box-shadow: 0 14px 30px var(--shadow);
    overflow: hidden;
  }

  /* Front */
  .card-front {
    display: flex;
    flex-direction: column;
    align-items: center;
    justify-content: center;
    gap: 18px;
  }
  .front-brand {
    display: flex;
    align-items: center;
    gap: 16px;
  }
  .brand-dot {
    width: 30px;
    height: 30px;
    border-radius: 50%;
    background: var(--accent-teal);
  }
  .brand-name {
    font-weight: 600;
    font-size: 50px;
    letter-spacing: 3px;
    color: var(--ink-navy);
  }
  .services {
    display: flex;
    align-items: center;
    gap: 12px;
    font-weight: 500;
    font-size: 12px;
    letter-spacing: 1.5px;
    text-transform: uppercase;
    color: var(--ink-muted);
  }
  .services-sep {
    width: 5px;
    height: 5px;
    border-radius: 50%;
    background: var(--accent-teal);
  }

  /* Back */
  .back-brand {
    position: absolute;
    left: 30px;
    top: 44px;
    display: flex;
    align-items: center;
    gap: 10px;
  }
  .back-brand .brand-dot { width: 18px; height: 18px; }
  .back-brand .brand-name { font-size: 26px; letter-spacing: 2px; }

  .holder {
    position: absolute;
    right: 40px;
    top: 56px;
    text-align: right;
  }
  .holder-name {
    font-weight: 700;
    font-size: 21px;
    letter-spacing: 0.5px;
    line-height: 26px;
  }
  .holder-title {
    margin-top: 2px;
    font-weight: 500;
    font-size: 11.5px;
    letter-spacing: 1px;
    text-transform: uppercase;
    color: var(--ink-muted);
  }
  .divider {
    position: absolute;
    left: 30px;
    right: 30px;
    top: 112px;
    height: 3px;
    background: var(--accent-teal);
  }
  .contact-list {
    position: absolute;
    left: 40px;
    top: 150px;
    list-style: none;
    font-weight: 500;
    font-size: 12.5px;
    line-height: 24px;
  }
  .phone-list {
    position: absolute;
    right: 40px;
    top: 124px;
    list-style: none;
    font-weight: 500;
    font-size: 12.5px;
    line-height: 22px;
  }
  .contact-list li, .phone-list li {
    display: flex;
    align-items: center;
    gap: 10px;
  }
  .icon { width: 13px; height: 13px; flex: none; }
  .corner-band {
    position: absolute;
    right: 0;
    bottom: 0;
    width: 500px;
    height: 286px;
    pointer-events: none;
  }
</style>
</head>
<body>

  <section class="card card-front" aria-label="Card front">
    <div class="front-brand">
      <span class="brand-dot" aria-hidden="true"></span>
      <span class="brand-name">VELORIX</span>
    </div>
    <p class="services">
      <span>Money Exchange</span>
      <span class="services-sep" aria-hidden="true"></span>
      <span>Cross-Border Remittance</span>
    </p>
  </section>

  <section class="card card-back" aria-label="Card back">
    <svg class="corner-band" viewBox="0 0 500 286" aria-hidden="true">
      <path d="M490 130 L500 130 L500 286 L0 286 L0 276 L452 276 Q462 276 466 268 L476 150 Q478 132 490 130 Z" fill="var(--band-navy)"/>
    </svg>

    <div class="back-brand">
      <span class="brand-dot" aria-hidden="true"></span>
      <span class="brand-name">VELORIX</span>
    </div>

    <div class="holder">
      <p class="holder-name">Marek Dalvin</p>
      <p class="holder-title">Managing Director</p>
    </div>
    <div class="divider" aria-hidden="true"></div>

    <ul class="phone-list">
      <li>
        <svg class="icon" viewBox="0 0 14 14" aria-hidden="true"><rect x="3.5" y="1" width="7" height="12" rx="1.5" fill="none" stroke="var(--accent-teal)" stroke-width="1.3"/></svg>
        318 62 7049
      </li>
      <li>
        <svg class="icon" viewBox="0 0 14 14" aria-hidden="true"><path d="M3 1.5 L5.5 1.5 L6.5 4.5 L5 5.5 Q6 8 8.5 9 L9.5 7.5 L12.5 8.5 L12.5 11 Q12 12.5 10.5 12.5 Q2 12 1.5 3.5 Q1.5 2 3 1.5 Z" fill="var(--accent-teal)"/></svg>
        318 62 7049
      </li>
    </ul>

    <ul class="contact-list">
      <li>
        <svg class="icon" viewBox="0 0 14 14" aria-hidden="true"><rect x="1" y="3" width="12" height="8.5" fill="var(--accent-teal)"/><path d="M1 3 L7 8 L13 3" fill="none" stroke="#fff" stroke-width="1.1"/></svg>
        youremail@email.com
      </li>
      <li>
        <svg class="icon" viewBox="0 0 14 14" aria-hidden="true"><path d="M7 1.5 L13 7 L11 7 L11 12.5 L3 12.5 L3 7 L1 7 Z" fill="var(--accent-teal)"/></svg>
        Your Home Address
      </li>
      <li>
        <svg class="icon" viewBox="0 0 14 14" aria-hidden="true"><circle cx="7" cy="7" r="5.6" fill="none" stroke="var(--accent-teal)" stroke-width="1.3"/><ellipse cx="7" cy="7" rx="2.4" ry="5.6" fill="none" stroke="var(--accent-teal)" stroke-width="1"/><line x1="1.4" y1="7" x2="12.6" y2="7" stroke="var(--accent-teal)" stroke-width="1"/></svg>
        Your Website
      </li>
    </ul>
  </section>

</body>
</html>
```